Build our new website pages and templates

BACKGROUND
• We are migrating over from an old website and URL ( www.plotmarker.co.nz ) to a brand new website with a new URL – www.halvoro.co.nz
• We have already selected a logo for the new website – see attached.
• We manage all our websites in house using Dreamweaver and want to retain the capability of doing this for the new site.

-------------------------------------------------------------------------------------

BRIEF
• Design the new look halvoro website for our company including color palette, fonts, icons, graphics and layout.

• The design should reflect our high quality venue hire services to corporate buyers, picking up inspiration from our beautiful new logo

• The index page should also incorporate our:

o What We Do page
o How To Use Our Site page
o Are you a venue? content (with link to the 'List A Venue' page)
o Our key contact links
o Our navigation menu

Here are some examples of the types of Index pages that appeal to us:

http://brightpebblelane.com/
What we like about it: Like the simplicity of the page and the scroll function to show different page elements.

http://www.trelbo.com/
What we like about it: Strong blocks of hero images and fonts. Easy scroll from one section to the next.

https://www.lumz.com/
What we like about it: Like the scroll feature to different sections.

https://www.plankhub.net/
What we like about it: Simple stylish Index page that scrolls easily

Our version would be:
1. Our logo centre page with hero image background
2. Scroll down to 'what we do' section with 3 bullet points and icons
3. Scroll down to 'how to use this site' section with 3 bullet points (1,2,3) and instructions
4. Are you a venue? instructions about how to talk to us about listing. And link to the 'how to list' page.

To the left we would want a burger menu with dropdown nav and links

• Design the template for the 'venue listings' pages
o We want to list venues by towns or cities and have one page dedicated for each. We would create each page from the template you provide.
o When the user clicks on any particular venue it clicks through to the individual venue page
o This page should have a map with pins for each listed venue

Here are some examples of the listings pages that we like and why:

http://www.trelbo.com/
What we like about it: Strong blocks and font. Nice hover feature changing the colour and introducing the click through arrow on the right bottom corner

http://www.roomtorrent.co.nz/
What we like about it: Don’t like the colours or design but like the practicality of the search box and the 3 column listings when you select a search criteria. This is a familiar format and maybe easier for the user to understand and navigate around.

http://www.harbourtix.co.nz/venues
What we like about it: Like the simplicity of this page but our listings would need a little more info beneath each one. The hover function is annoying!

• Design the template for the individual venue pages.
• Include a search function across the full site so that users can choose to search for venues in different towns or cities.
• Design the booking form pages for the individual venues (we have working examples of our existing ones)

• Design the payment page and thank you page for those who complete the booking form online. (We will be offering the option on our site to pay by credit card into our coinvale account) We have working examples of our current thank you and payment page although the payment page is not live on our current site.

------------------------------------------------------------------------------------

TECHNICAL
• Pages need to be created in html and css. Some php pages, as required for payment pages. And some javascript for all pages.

• Templates will need to be in dwt format, as we need to be able to upload to Dreamweaver CC and create new pages from the templates for new venues as and when necessary.

• Pages should be responsive for browsing across PC’s Laptops, ipads, phones and other devices.

• Website will be hosted on a Linux server when ready to go live.

A) We can provide existing website files if these help with the design and build process of the new site.
B) We plan to build additional features for the site, as a second phase project. This would include client login areas and electronic confirmations of bookings and online updating of booking forms.

• See the brief provided. Successful designer/developer must be able to supply files in html, css, php (if required) and include javascript coding where necessary. We will be hosting these files and managing the site using Dreamweaver CC so full accessibility to the files is important.
• Notes have been added to the brief. Please read and ask questions if not clear.
• We are not looking for a site to be built using an open source platform. The files provided must be able to be uploaded to our own server for our own management after the end of the project.

```html
<!DOCTYPE html>
<html lang="en">
<head>
<meta charset="utf-8">
<title>Halvoro — Finding Venues For You</title>
<link href="https://fonts.googleapis.com/css2?family=Raleway:wght@300;600;700;800&family=Open+Sans:wght@400;600;700&display=swap" rel="stylesheet">
<style>
:root{
  --ink:#231f20;
  --ink-soft:#2b2728;
  --ring:#6a6668;
  --white:#ffffff;
  --muted:#e6e3e0;
  --gold:#d99b2b;
  --wood:#8a5a32;
  --stone:#8d8275;
}
*{margin:0;padding:0;box-sizing:border-box}
html,body{width:719px;height:1200px;overflow:hidden;background:var(--ink)}
body{position:relative;font-family:"Open Sans",sans-serif;color:var(--white)}
.abs{position:absolute}
.center{left:0;width:719px;text-align:center}

/* header */
.site-header{top:0;left:0;width:719px;height:52px;background:var(--ink);z-index:3}
.menu-btn{left:44px;top:13px;width:26px;height:26px;border:1.5px solid var(--white);border-radius:50%}
.search-btn{left:649px;top:19px}
.brand-disc{left:297px;top:-29px;width:124px;height:124px;border-radius:50%;background:var(--ink);z-index:4;text-align:center}
.brand-name{position:absolute;left:0;width:124px;top:80px;font-family:"Raleway",sans-serif;font-weight:300;font-size:15px;letter-spacing:.5px;color:var(--white)}

/* hero */
.hero{top:52px;left:0;width:719px;height:302px;background:linear-gradient(180deg,#6d5a3c 0%,#a08a63 25%,#8e8579 55%,#b3aba0 100%)}
.hero-title{top:183px;font-family:"Raleway",sans-serif;font-weight:800;font-size:35px;letter-spacing:-.3px;text-shadow:0 2px 6px rgba(0,0,0,.55)}

/* what we do */
.what{top:354px;left:0;width:719px;height:328px;background:var(--ink)}
.section-title{font-family:"Raleway",sans-serif;font-weight:700;font-size:24px;letter-spacing:.2px}
.intro{font-size:7.3px;line-height:15px;color:var(--muted)}
.feature{width:210px;text-align:center}
.feature-ring{margin:0 auto;width:104px;height:104px;border:2px solid var(--ring);border-radius:50%;display:flex;align-items:center;justify-content:center}
.feature-title{margin-top:15px;font-family:"Raleway",sans-serif;font-weight:600;font-size:11px}
.feature-list{list-style:none;margin-top:8px;font-size:7.3px;line-height:14.5px;color:var(--muted)}
.feature-list li::before{content:"✔";margin-right:5px;font-size:7px}

/* how to */
.how-photo{top:682px;left:359px;width:360px;height:279px;background:linear-gradient(160deg,#6f7d78 0%,#8a5a32 45%,#b07a46 75%,#3a2a20 100%)}
.how-panel{top:682px;left:0;width:359px;height:279px;background:linear-gradient(180deg,#1c1a1b 0%,#2a2522 60%,#1e1b1a 100%)}
.how-title{left:59px;top:714px;font-family:"Raleway",sans-serif;font-weight:700;font-size:24px}
.how-text{left:60px;top:756px;width:290px;font-size:7.3px;line-height:15px;color:var(--muted)}
.how-list{left:60px;top:819px;list-style:none;font-size:8.4px;color:var(--muted)}
.how-list li{height:30px}
.how-list li::before{content:"✔";margin-right:7px;font-size:8px}
.read-more{left:59px;top:913px;font-size:7.8px;font-weight:700;color:var(--white);text-decoration:none}

/* venue cta */
.venue{top:961px;left:0;width:719px;height:190px;background:var(--gold)}
.venue-title{top:993px;font-family:"Raleway",sans-serif;font-weight:700;font-size:22px}
.venue-text{top:1031px;left:110px;width:499px;font-size:7.3px;line-height:16.5px;text-align:center}
.venue-btn{left:298px;top:1094px;width:124px;height:25px;background:var(--ink);border:1.5px solid var(--white);font-size:9px;font-weight:700;line-height:22px;text-align:center;color:var(--white);text-decoration:none}

/* footer */
.site-footer{top:1151px;left:0;width:719px;height:49px;background:var(--ink)}
.copyright{left:59px;top:1169px;font-size:7.2px;color:var(--muted)}
.social{top:1166px;left:557px;display:flex;gap:8.6px}
.social span{width:14px;height:14px;border-radius:3px;background:var(--white);display:block}
</style>
</head>
<body>

<header class="abs site-header">
  <div class="abs menu-btn">
    <svg width="26" height="26" viewBox="0 0 26 26" style="position:absolute;left:-1.5px;top:-1.5px"><g stroke="#fff" stroke-width="1.6"><line x1="9" y1="9.5" x2="17" y2="9.5"/><line x1="9" y1="13" x2="17" y2="13"/><line x1="9" y1="16.5" x2="17" y2="16.5"/></g></svg>
  </div>
  <svg class="abs search-btn" width="14" height="14" viewBox="0 0 14 14"><circle cx="5.5" cy="5.5" r="4" fill="none" stroke="#fff" stroke-width="1.8"/><line x1="8.5" y1="8.5" x2="12" y2="12" stroke="#fff" stroke-width="2"/></svg>
</header>
<div class="abs brand-disc"><span class="brand-name">HALVORO</span></div>

<section class="abs hero" role="img" aria-label="Photo of an empty conference hall with timber ceiling and patterned carpet"></section>
<h1 class="abs center hero-title">FINDING VENUES FOR YOU</h1>
<svg class="abs" style="left:30px;top:192px" width="12" height="22" viewBox="0 0 12 22"><polyline points="11,1 1,11 11,21" fill="none" stroke="rgba(255,255,255,.6)" stroke-width="1.5"/></svg>
<svg class="abs" style="left:677px;top:192px" width="12" height="22" viewBox="0 0 12 22"><polyline points="1,1 11,11 1,21" fill="none" stroke="rgba(255,255,255,.6)" stroke-width="1.5"/></svg>
<svg class="abs" style="left:349px;top:300px" width="21" height="12" viewBox="0 0 21 12"><polyline points="1,1 10.5,10 20,1" fill="none" stroke="#fff" stroke-width="2"/></svg>

<section class="abs what"></section>
<h2 class="abs center section-title" style="top:385px">WHAT WE DO</h2>
<p class="abs center intro" style="top:423px">We are your professional conference and event organisers, providing you with multiple venue options and conference solutions all in<br>one place. Why spend hours searching for venues and contacing each one when we'll do all that for you.</p>

<div class="abs feature" style="left:45px;top:476px">
  <div class="feature-ring">
    <svg width="60" height="72" viewBox="0 0 60 72" fill="none" stroke="#fff" stroke-width="1.6"><circle cx="30" cy="28" r="24"/><circle cx="30" cy="28" r="16"/><polygon points="30,18 33,25 40,25 34.5,29.5 37,37 30,32.5 23,37 25.5,29.5 20,25 27,25"/><path d="M18 48 L12 66 L19 62 L22 69 L27 52"/><path d="M42 48 L48 66 L41 62 L38 69 L33 52"/></svg>
  </div>
  <div class="feature-title">QUALITY &amp; HIGH SERVICE</div>
  <ul class="feature-list"><li>At vero eos et accusadrtmus et iusto</li><li>ducimus qui blanditiis praesentium voluptatum</li><li>At vero eos et accusamuyuts et iusto</li></ul>
</div>
<div class="abs feature" style="left:255px;top:476px">
  <div class="feature-ring">
    <svg width="60" height="66" viewBox="0 0 60 66" fill="none" stroke="#fff" stroke-width="1.6"><circle cx="30" cy="38" r="25"/><circle cx="30" cy="38" r="19"/><rect x="24" y="2" width="12" height="7" rx="2"/><line x1="30" y1="9" x2="30" y2="13"/><line x1="50" y1="16" x2="54" y2="12"/><line x1="30" y1="38" x2="19" y2="28"/><circle cx="30" cy="38" r="2"/></svg>
  </div>
  <div class="feature-title">TIME SAVING</div>
  <ul class="feature-list"><li>At vero eos et accusadrtmus et iusto</li><li>ducimus qui blanditiis praesentium voluptatum</li><li>At vero eos et accusamuyuts et iusto</li></ul>
</div>
<div class="abs feature" style="left:465px;top:476px">
  <div class="feature-ring">
    <svg width="76" height="66" viewBox="0 0 76 66" fill="none" stroke="#fff" stroke-width="1.5"><circle cx="38" cy="12" r="8"/><path d="M24 38 C24 24 52 24 52 38 Z"/><circle cx="20" cy="18" r="6"/><path d="M8 38 C8 28 22 26 26 30"/><circle cx="56" cy="18" r="6"/><path d="M68 38 C68 28 54 26 50 30"/><g stroke-width="1.2"><polygon points="10,48 11.5,51 15,51 12.3,53 13.3,56 10,54 6.7,56 7.7,53 5,51 8.5,51"/><polygon points="24,52 25.5,55 29,55 26.3,57 27.3,60 24,58 20.7,60 21.7,57 19,55 22.5,55"/><polygon points="38,55 39.5,58 43,58 40.3,60 41.3,63 38,61 34.7,63 35.7,60 33,58 36.5,58"/><polygon points="52,52 53.5,55 57,55 54.3,57 55.3,60 52,58 48.7,60 49.7,57 47,55 50.5,55"/><polygon points="66,46 67.5,49 71,49 68.3,51 69.3,54 66,52 62.7,54 63.7,51 61,49 64.5,49"/></g></svg>
  </div>
  <div class="feature-title">CUSTOMER SATISFACTION</div>
  <ul class="feature-list"><li>At vero eos et accusadrtmus et iusto</li><li>ducimus qui blanditiis praesentium voluptatum</li><li>At vero eos et accusamuyuts et iusto</li></ul>
</div>

<section class="abs how-photo" role="img" aria-label="Photo of a training room with timber desks, office chairs and a projector screen"></section>
<section class="abs how-panel" role="img" aria-label="Darkened photo of rows of conference desks"></section>
<h2 class="abs how-title">HOW TO USE THIS SITE</h2>
<p class="abs how-text">Nam libero tempore, cum soluta nobis est eligendi optio cumque nihil impedit quo minus id quod maxime placeat facere possimus, omnis voluptas assumen da est, omnis dolor repellendus.</p>
<ul class="abs how-list">
  <li>Ut enim ad minima veniam, quis nostrum exercitatione</li>
  <li>Itaque earum rerum hic tenetur a sapiente delectus</li>
  <li>Temporibus autem quibusdam et aut officiis debitis aut</li>
</ul>
<a class="abs read-more" href="#">READ MORE &gt;&gt;</a>

<section class="abs venue"></section>
<h2 class="abs center venue-title">ARE YOU A VENUE?</h2>
<p class="abs venue-text">Sed ut perspiciatis unde omnis iste natus error sit voluptatem accusantium doloremque laudantium, totam rem aperiam, eaque ipsa quae ab illo inventore veritatis et quasi architecto beatae vitae dicta sunt explicabo. Nemo enim ipsam voluptatem quia voluptas sit aspernatur aut odit aut fugit, sed quia consequuntur magni dolores eos qui ratione</p>
<a class="abs venue-btn" href="#">LIST A VENUE</a>

<footer class="abs site-footer"></footer>
<p class="abs copyright">Copyrights © 2016, Halvoro.&nbsp; All rights reserved.</p>
<div class="abs social" aria-label="Social links"><span></span><span></span><span></span><span></span><span></span></div>

</body>
</html>
```